Banner design

I need a banner designed that we will be putting on our gym walls. We need two banners but both will have the same design:
- One will be printed 12.2 X 2.5m
- One will be printed 9.4 X 2.5m
We are a kids gymnastics and cheerleading gym so are looking for something bright and fun that still looks professional.
Our colours are lime green, navy blue and white.
I have uploaded a couple of examples of what other gyms have done.
Kids

```html
<!DOCTYPE html>
<html lang="en">
<head>
<meta charset="UTF-8">
<title>Vaultline Gymsports Banner</title>
<link rel="stylesheet" href="https://fonts.googleapis.com/css2?family=Oswald:wght@500;700&family=Montserrat:wght@600;700&family=Open+Sans:wght@400&display=swap">
<style>
  :root {
    --lime: #8fd62a;
    --lime-light: #a6e33a;
    --lime-pale: #c9f07a;
    --navy: #1b2d4f;
    --slate: #3d5048;
    --white: #ffffff;
    --grey: #5c6b5c;
    --photo-top: #dfe6df;
    --photo-bottom: #f4f4f2;
  }
  * { box-sizing: border-box; margin: 0; padding: 0; }
  html, body { width: 1200px; height: 249px; overflow: hidden; background: var(--white); }
  .banner {
    position: relative;
    width: 1200px;
    height: 249px;
    overflow: hidden;
    font-family: "Oswald", sans-serif;
  }
  .banner__backdrop { position: absolute; inset: 0; }

  .brand {
    position: absolute;
    left: 26px;
    top: 62px;
    width: 230px;
    text-align: center;
  }
  .brand__name {
    display: flex;
    align-items: center;
    justify-content: center;
    gap: 8px;
    font-family: "Montserrat", sans-serif;
    font-weight: 700;
    color: var(--navy);
    line-height: 1;
  }
  .brand__mark {
    width: 18px; height: 18px;
    border-radius: 50%;
    background: var(--navy);
    flex: none;
  }
  .brand__word { font-size: 30px; letter-spacing: 0.5px; }
  .brand__sub {
    font-family: "Montserrat", sans-serif;
    font-weight: 700;
    color: var(--navy);
    font-size: 22px;
    letter-spacing: 2px;
    margin-top: 6px;
  }
  .brand__web {
    font-family: "Open Sans", sans-serif;
    font-size: 11.5px;
    color: var(--navy);
    letter-spacing: 1.6px;
    margin-top: 14px;
  }

  .quote {
    position: absolute;
    left: 436px;
    top: 68px;
    width: 338px;
    height: 104px;
    display: flex;
    align-items: center;
    justify-content: center;
  }
  .quote__frame { position: absolute; inset: 0; }
  .quote__text {
    position: relative;
    font-weight: 500;
    font-size: 20px;
    line-height: 1.45;
    color: var(--slate);
    text-align: center;
    text-transform: uppercase;
    letter-spacing: 0.3px;
  }
  .quote__author {
    position: absolute;
    left: 664px;
    top: 205px;
    font-family: "Open Sans", sans-serif;
    font-size: 13.5px;
    color: var(--grey);
  }

  .coach-photo {
    position: absolute;
    left: 805px;
    top: 28px;
    width: 196px;
    height: 221px;
    border-radius: 90px 90px 0 0;
    background: linear-gradient(180deg, var(--photo-top), var(--photo-bottom));
  }
</style>
</head>
<body>
<div class="banner">
  <svg class="banner__backdrop" width="1200" height="249" viewBox="0 0 1200 249" aria-hidden="true">
    <rect width="1200" height="249" fill="var(--white)"/>
    <polygon points="290,0 1200,0 1200,249 220,249" fill="var(--lime)"/>
    <g stroke-linecap="round" fill="none">
      <g stroke="var(--lime-light)" stroke-width="14">
        <line x1="250" y1="240" x2="400" y2="30"/>
        <line x1="330" y1="260" x2="420" y2="140"/>
        <line x1="650" y1="50" x2="700" y2="-20"/>
        <line x1="690" y1="90" x2="770" y2="-20"/>
        <line x1="690" y1="270" x2="760" y2="180"/>
        <line x1="760" y1="270" x2="810" y2="205"/>
        <line x1="1080" y1="120" x2="1160" y2="10"/>
      </g>
      <g stroke="var(--lime-pale)" stroke-width="10">
        <line x1="380" y1="50" x2="420" y2="-10"/>
        <line x1="420" y1="90" x2="470" y2="20"/>
        <line x1="1080" y1="40" x2="1110" y2="0"/>
      </g>
      <g stroke="var(--lime-pale)" stroke-width="14" opacity="0.7">
        <line x1="60" y1="30" x2="90" y2="-10"/>
        <line x1="20" y1="40" x2="55" y2="-10"/>
      </g>
      <g stroke="var(--white)" stroke-width="18">
        <line x1="1110" y1="250" x2="1200" y2="130"/>
        <line x1="1160" y1="260" x2="1210" y2="190"/>
        <line x1="1060" y1="260" x2="1120" y2="180"/>
        <line x1="1180" y1="20" x2="1210" y2="-20"/>
      </g>
    </g>
  </svg>

  <div class="brand">
    <div class="brand__name">
      <span class="brand__mark"></span>
      <span class="brand__word">VAULTLINE</span>
    </div>
    <div class="brand__sub">GYMSPORTS</div>
    <div class="brand__web">www.vaultlinegym.com</div>
  </div>

  <div class="quote">
    <svg class="quote__frame" width="338" height="104" viewBox="0 0 338 104" aria-hidden="true">
      <path d="M40 1 H337 V103" fill="none" stroke="var(--slate)" stroke-width="1.2" opacity="0.75"/>
      <path d="M298 103 H1 V1" fill="none" stroke="var(--slate)" stroke-width="1.2" opacity="0.75"/>
      <text x="10" y="18" font-family="Oswald, sans-serif" font-weight="700" font-size="28" fill="var(--slate)">“</text>
      <text x="310" y="124" font-family="Oswald, sans-serif" font-weight="700" font-size="28" fill="var(--slate)">”</text>
    </svg>
    <p class="quote__text">We are a kids gymnastics and<br>cheerleading gym</p>
  </div>
  <p class="quote__author">Mia Carter</p>

  <div class="coach-photo" role="img" aria-label="Photo of a smiling young coach in a white club polo shirt"></div>
</div>
</body>
</html>
```